Portal for Beautiful & Up-and-Coming Caribbean destination of KVT, Puerto Rico

We need the web design of an online portal for the KVT community of Puerto Rico. This should include the landing page, menu page, and at least one content page. The KVT area is a vibrant area in Northwest Puerto Rico with an airport, many local restaurants, beautiful beaches, and many things to do. I attach the logo which should be featured prominently, and we'll also be selling merchandise using this logo. The website should be a place for everyone in the community or tourists looking for things to do and places to stay. It will need to feature space and places for advertising as well. Also, we have a live hashtag feed (www.kvtvibe-demo.com) where businesses and people in the community can hashtag their posts (we have licensed software that updates it every 30 minutes). We would like for the live hashtag feed to be part of the design, though the format can be changed a bit from what is currently in place. Indeed, the landing page should be changed to emphasize both the hashtag feed as well as the content of the site of KVTvibe. We need the landing page, menu page which will include 10-15 different modules or pages (examples: restaurants, things to do, places to stay, flights). I attach a spreadsheet which shows the menu pages that need to be featured. Comparable websites in our area are www.gosulena.com and www.varelaguide.com (but I don't like either one!). The final design should be contemporary, fresh, colorful fun and current, and communicate a vibrant and interactive community.

Target Market(s)

Tourists and people who live in this beach - oriented, beautiful community

Industry/Entity Type

Community

Number of Pages Required

3 page

Font styles to use
Sans Serif

Colors
33a6d7
f68e4e

Requirements
Must have
• landing page, menu design/page, and a sample content page. It must integrate a live hashtag feed, comparable to what is currently seen on www.kvtvibe-demo.com. It must be fun, contemporary, colorful, unique, and clean. It must allow for advertising space.
Nice to have
• comments and interaction with visitors. Colors that integrate with the logo. Much emphasis on the logo, as we will also be selling merchandise.
Should not have
• extra squiggles and curlies and adornments.

```html
<!DOCTYPE html>
<html lang="en">
<head>
<meta charset="utf-8">
<title>KVTvibe – Portal</title>
<link rel="stylesheet" href="https://fonts.googleapis.com/css2?family=Lato:wght@400;700;900&family=Montserrat:wght@400;500;600&display=swap">
<style>
:root{
  --blue:#33a6d7;
  --orange:#f68e4e;
  --ink:#222;
  --muted:#555;
  --soft:#f4f4f4;
  --footer:#3a3a3a;
  --footer-dark:#2b2b2b;
  --white:#fff;
}
*{box-sizing:border-box;margin:0;padding:0}
html,body{width:1200px;height:3871px;overflow:hidden}
body{font-family:"Lato",sans-serif;color:var(--ink);background:var(--white);position:relative}
.abs{position:absolute}
h1,h2,h3,.menu,.title{font-family:"Montserrat",sans-serif}

/* hero */
.hero{left:0;top:0;width:1200px;height:608px;background:linear-gradient(180deg,#6fb8e6 0%,#9fd3ef 35%,#3cc3c9 62%,#18a3b2 100%)}
.topbar{left:60px;top:26px;width:1080px;height:114px;background:rgba(255,255,255,.96)}
.logo{left:18px;top:22px;font-family:"Lato",sans-serif;font-weight:900;font-size:44px;color:var(--blue);display:flex;align-items:center;gap:10px}
.logo .dot{width:18px;height:18px;border-radius:50%;background:var(--orange)}
.contact{top:16px;display:flex;align-items:center;gap:10px;font-size:15px}
.contact small{display:block;color:var(--blue);font-size:11px}
.social{right:18px;top:20px;display:flex;gap:6px}
.social i{width:20px;height:20px;border-radius:50%;background:var(--orange);display:block}
.menu{right:12px;top:70px;display:flex;font-size:15px;font-weight:500;color:#333}
.menu span{padding:9px 14px}
.menu .active{background:var(--orange);color:var(--white)}
.hero-brand{left:0;width:1200px;top:290px;text-align:center;color:var(--white);font-weight:900;font-size:78px;letter-spacing:2px}
.hero-tag{left:0;width:1200px;top:385px;text-align:center;color:var(--white);font-family:"Montserrat",sans-serif;font-weight:500;font-size:38px;text-shadow:0 2px 6px rgba(0,0,0,.3)}

/* why */
.sec-title{left:0;width:1200px;text-align:center;font-family:"Montserrat",sans-serif;font-size:40px;font-weight:500;color:#111}
.sec-title b{color:var(--blue);font-weight:500}
.sec-title .or{color:var(--orange)}
.underline{height:2px;background:#222;left:445px;width:310px}
.quote{left:120px;width:960px;top:756px;text-align:center;font-size:14px;line-height:27px;color:#333}
.avatar{left:432px;top:878px;width:132px;height:132px;border-radius:50%;border:5px solid #eee;background:linear-gradient(160deg,#7aa368,#d8d2c4)}
.author{left:582px;top:905px}
.author small{font-size:12px;color:#444}
.author h3{font-size:22px;font-weight:600;margin:2px 0 8px}
.btn{display:inline-block;background:var(--blue);color:var(--white);font-size:15px;padding:8px 14px;font-family:"Montserrat",sans-serif}

/* interests */
.interests{left:0;top:1110px;width:1200px;height:1064px;background:var(--soft)}
.sub{left:0;width:1200px;text-align:center;color:var(--orange);font-size:13px}
.card{background:#888;overflow:hidden}
.card .cap{position:absolute;left:8px;bottom:14px;right:40%;min-width:230px;background:rgba(51,166,215,.9);color:var(--white);padding:6px 10px 6px 56px}
.card .cap::before{content:"";position:absolute;left:10px;top:8px;width:30px;height:30px;border-radius:50%;background:var(--orange)}
.card .cap h3{font-family:"Montserrat",sans-serif;font-size:24px;font-weight:500;line-height:28px}
.card .cap p{font-size:11px}
.btn-or{left:478px;top:2053px;width:244px;height:46px;background:var(--orange);color:var(--white);font-family:"Montserrat",sans-serif;font-size:19px;display:flex;align-items:center;justify-content:center;gap:10px}
.btn-or i{width:20px;height:20px;background:var(--white);border-radius:3px;display:block}

/* guides */
.book-back{left:76px;top:2435px;width:260px;height:360px;background:linear-gradient(180deg,#3aa86a,#8ec94a 70%,#5ab23e);box-shadow:0 6px 14px rgba(0,0,0,.25)}
.book-front{left:150px;top:2290px;width:318px;height:560px;background:linear-gradient(180deg,#2a9ee0 0%,#55b7ea 45%,#c44 72%,#f3f3f3 100%);transform:rotate(8deg);box-shadow:0 10px 24px rgba(0,0,0,.3)}
.book-front .bt{position:absolute;left:40px;top:40px;color:var(--white);font-weight:900}
.book-front .bt span{display:block;font-size:24px}
.book-front .bt strong{display:block;font-size:60px;line-height:62px;margin-top:20px}
.guides-title{left:706px;top:2378px;font-family:"Montserrat",sans-serif;font-size:50px;color:var(--orange);font-weight:400}
.price{left:716px;top:2442px;font-size:15px}
.guides-text{left:706px;top:2500px;width:360px;font-size:21px;line-height:33px;color:#333}
.goto{left:706px;top:2618px}
.dots{left:710px;top:2708px;display:flex;gap:6px}
.dots i{width:11px;height:11px;border-radius:50%;background:var(--orange);display:block}
.dots i:first-child{background:#111}

/* community */
.community{left:0;top:2930px;width:1200px;height:561px;background:var(--soft)}
.ccard{top:3080px;width:266px;height:362px}
.ccard .tag{position:absolute;top:0;left:50%;transform:translateX(-50%);width:130px;text-align:center;color:var(--white);font-family:"Montserrat",sans-serif;font-size:15px;font-weight:600;padding:5px 0}
.ccard .txt{position:absolute;left:12px;right:10px;bottom:14px;color:var(--white)}
.ccard h3{font-family:"Montserrat",sans-serif;font-size:24px;font-weight:600}
.ccard p{font-size:16px;line-height:18px}

/* footer */
.footer{left:0;top:3491px;width:1200px;height:330px;background:var(--footer)}
.fcol{top:3540px;color:var(--white)}
.fcol h4{font-family:"Montserrat",sans-serif;color:var(--blue);font-size:20px;font-weight:600;margin-bottom:10px}
.fcol li{list-style:none;font-size:13px;line-height:19px}
.fsocial{display:flex;gap:10px;margin-bottom:10px}
.fsocial i{width:18px;height:18px;border-radius:50%;background:var(--white);display:block}
.fcol .hint{font-size:12px;margin-bottom:8px}
.subscribe{display:flex;width:256px;height:38px}
.subscribe span{flex:1;background:var(--white);color:#999;font-size:12px;padding:11px 8px}
.subscribe b{width:50px;background:var(--orange);display:flex;align-items:center;justify-content:center}
.copy{left:0;top:3821px;width:1200px;height:50px;background:var(--footer-dark);color:#ddd;font-size:13px;text-align:center;line-height:50px}
</style>
</head>
<body>

<header>
  <div class="abs hero" role="img" aria-label="Photo of turquoise Caribbean sea with a beach house, palm trees and a pelican"></div>
  <div class="abs topbar">
    <div class="abs logo"><span class="dot"></span>KVTvibe</div>
    <div class="abs contact" style="left:540px">
      <svg width="34" height="24" viewBox="0 0 34 24"><rect x="1" y="1" width="32" height="22" fill="#222"/><path d="M1 1 L17 13 L33 1" stroke="#fff" stroke-width="2" fill="none"/></svg>
      <div><small>Mail us</small>hello@kvtvibe-demo.com</div>
    </div>
    <div class="abs contact" style="left:765px">
      <svg width="26" height="26" viewBox="0 0 24 24"><path d="M6.6 10.8a15 15 0 0 0 6.6 6.6l2.2-2.2a1 1 0 0 1 1-.25 11.4 11.4 0 0 0 3.6.57 1 1 0 0 1 1 1V20a1 1 0 0 1-1 1A17 17 0 0 1 3 4a1 1 0 0 1 1-1h3.5a1 1 0 0 1 1 1 11.4 11.4 0 0 0 .57 3.6 1 1 0 0 1-.25 1z" fill="#222"/></svg>
      <div><small>Call now!</small>+100 555 0142</div>
    </div>
    <div class="abs social"><i></i><i></i><i></i><i></i></div>
    <nav class="abs menu"><span class="active">HOME</span><span>DOING BUSINESS</span><span>ABOUT US</span><span>STATISTICS</span><span>EVENTS</span><span>PRESS ROOM</span><span>CONTACT US</span></nav>
  </div>
  <div class="abs hero-brand">KVT</div>
  <h1 class="abs hero-tag">IS BRINGING IN THE CATCH OF THE DAY</h1>
</header>

<section>
  <h2 class="abs sec-title" style="top:668px">WHY I LOVE <b>KVT</b></h2>
  <div class="abs underline" style="top:724px"></div>
  <p class="abs quote">“It was a balmy January evening on a back street of Old San Juan and I noticed a tiny corner bar where a TV was showing a football game being played in a blizzard. How could I not walk right in, order a cold beer, and enjoy the incongruity? Later, as the night progressed, I was struck by the local families out strollt could easily be just a cliché. The next day it was…”</p>
  <div class="abs avatar" role="img" aria-label="Portrait photo of the article writer"></div>
  <div class="abs author"><small>Lena Ortal</small><h3>Article Writer</h3><span class="btn">Read More</span></div>
</section>

<section>
  <div class="abs interests"></div>
  <h2 class="abs sec-title" style="top:1160px">DISCOVER KVT BY INTEREST</h2>
  <p class="abs sub" style="top:1218px">See where people are traveling, all around the world.</p>

  <div class="abs card" style="left:60px;top:1287px;width:723px;height:330px;background:linear-gradient(180deg,#8fb2cf,#c2553f 45%,#7a6a5a)" role="img" aria-label="Photo of a waterfront restaurant terrace with red umbrellas">
    <div class="cap"><h3>Places to Eat</h3><p>Hit the ground at the right time</p></div></div>
  <div class="abs card" style="left:828px;top:1287px;width:312px;height:330px;background:linear-gradient(180deg,#9cc9e4,#e8e4df 55%,#4a87a8)" role="img" aria-label="Photo of a wedding couple by the sea">
    <div class="cap"><h3>Wedding</h3><p>Hit the ground at the right time</p></div></div>
  <div class="abs card" style="left:60px;top:1664px;width:326px;height:324px;background:linear-gradient(180deg,#5d9ad0,#c9a87a 50%,#6f8f4a)" role="img" aria-label="Photo of a resort hotel building with palm trees">
    <div class="cap"><h3>Hotels &amp; Resorts</h3><p>Hit the ground at the right time</p></div></div>
  <div class="abs card" style="left:441px;top:1664px;width:326px;height:324px;background:linear-gradient(135deg,#3e5a4a,#d9c7a6 50%,#a8563c)" role="img" aria-label="Photo of dim sum dishes on a table">
    <div class="cap"><h3>Food &amp; Drinks</h3><p>Hit the ground at the right time</p></div></div>
  <div class="abs card" style="left:828px;top:1664px;width:312px;height:324px;background:linear-gradient(180deg,#1b1f4a,#c33b7d 45%,#2e9ad8)" role="img" aria-label="Photo of a vivid sunset with palm silhouettes">
    <div class="cap"><h3>Sunset Night</h3><p>Hit the ground at the right time</p></div></div>

  <div class="abs btn-or"><i></i>Read More Things</div>
</section>

<section>
  <div class="abs book-back" role="img" aria-label="Travel guidebook cover about Caribbean islands"></div>
  <div class="abs book-front" role="img" aria-label="Travel guidebook cover for Puerto Rico with a painted boat">
    <div class="bt"><span>KVTvibe</span><strong>Puerto<br>Rico</strong></div>
  </div>
  <h2 class="abs guides-title">Travel Guides</h2>
  <p class="abs price">Starting at $14.99</p>
  <p class="abs guides-text">Ready to go? Get to the heart of Puerto Rico with one of in-depth, award-winning guidebooks.</p>
  <span class="abs btn goto">&#128722; Goto Store</span>
  <div class="abs dots"><i></i><i></i><i></i><i></i><i></i></div>
</section>

<section>
  <div class="abs community"></div>
  <h2 class="abs sec-title" style="top:2985px">OUR <span class="or">COMMUNITY</span></h2>
  <div class="abs underline" style="top:3040px;left:425px;width:350px"></div>

  <div class="abs ccard" style="left:60px;background:linear-gradient(180deg,#9cc8e8,#4a78a4 60%,#3d5a6a)" role="img" aria-label="Photo of a child looking out to sea">
    <div class="tag" style="background:var(--blue)">Your KVT</div>
    <div class="txt"><h3>Make KVT yours</h3><p>Create your symbol, Tell your story</p></div></div>
  <div class="abs ccard" style="left:333px;background:linear-gradient(180deg,#a6c8de,#3d9bbf 40%,#4f7a3a)" role="img" aria-label="Aerial photo of a green coastline and bay">
    <div class="tag" style="background:#555">Traveling</div>
    <div class="txt"><h3>Tomas &amp; Inez</h3><p>Across an ocean or across town, Tomas &amp; Inez are in search of local experiences</p></div></div>
  <div class="abs ccard" style="left:604px;background:linear-gradient(180deg,#3b4a5a,#9fb6c9 40%,#6a5a4a)" role="img" aria-label="Photo of a traveler at a stone arch">
    <div class="tag" style="background:var(--orange)">Business</div>
    <div class="txt"><h3>Business Travel</h3><p>Feel at home, wherever your work takes you. Feel at home.</p></div></div>
  <div class="abs ccard" style="left:877px;width:263px;background:linear-gradient(180deg,#1f4f7a,#2a6a8f 50%,#12344f)" role="img" aria-label="Underwater photo of a scuba diver">
    <div class="tag" style="background:#111">Hosting</div>
    <div class="txt"><h3>Hosting</h3><p>A professional photographer guests explore Harbor's arts</p></div></div>
</section>

<footer>
  <div class="abs footer"></div>
  <div class="abs fcol" style="left:60px"><h4>Destinations</h4><ul><li>Africa</li><li>Antarctica</li><li>Asia</li><li>Caribbean Islands</li><li>Central America</li><li>Europe</li><li>Middle East</li><li>North America</li><li>Pacific</li><li>South America</li></ul></div>
  <div class="abs fcol" style="left:258px"><h4>Shop</h4><ul><li>Destination guides</li><li>eBooks</li><li>Pictorial &amp; gifts</li><li>Phrasebooks</li><li>Activity guides</li><li>Special offers</li></ul></div>
  <div class="abs fcol" style="left:443px"><h4>Forums</h4><ul><li>Country forums</li><li>Talk to Wander Atlas</li><li>Interest forums</li><li>Travel buddies &amp; for sale</li></ul></div>
  <div class="abs fcol" style="left:660px"><h4>Interests</h4><ul><li>Adventure travel</li><li>Beaches</li><li>Budget travel</li><li>Family travel</li><li>Festivals and events</li><li>Food and drink</li><li>Honeymoons and romance</li><li>Luxury travel</li><li>Round the world travel</li><li>Wildlife and nature</li></ul></div>
  <div class="abs fcol" style="left:888px"><h4>Subscribe</h4>
    <div class="fsocial"><i></i><i></i><i></i><i></i></div>
    <p class="hint">Subscribe here with email to get latest news</p>
    <div class="subscribe"><span>Your Email</span><b><svg width="20" height="20" viewBox="0 0 24 24"><path d="M2 12 22 3 15 22 12 13z" fill="#fff"/></svg></b></div>
  </div>
  <div class="abs copy">Copyright © 2016 KVTVIBE-DEMO.COM, Inc. All Rights Reserved</div>
</footer>

</body>
</html>
```